Vantoro Poster Design

We need posters for in store(liquor store) promotions. Something that will stand out amongst a clutter of posters.
Updates

Email me at mdresner@lumavex.com subject "vantoro poster" for a copy of the can design. If need to help with the poster design.  

Target Market(s)

18 to 25 year old male and females, The target market sets and flows trends.

Requirements
Must have
• If any of the following are use is must be followed by tm.
• - product name "Vantoro"
• - Slogan "experience the magic"
• - The Vantoro Logo
Should not have
• No one drink anything, ex. a girl drinking water
• No one sipping on a drink

```html
<!DOCTYPE html>
<html lang="en">
<head>
<meta charset="utf-8">
<title>Vantoro – Experience the Magic</title>
<link rel="stylesheet" href="https://fonts.googleapis.com/css2?family=Anton&display=swap">
<style>
  :root {
    --red-top: #e01c00;
    --red-mid: #ea5a22;
    --orange-glow: #fdb662;
    --red-low: #e8461e;
    --white: #ffffff;
    --ghost: rgba(255, 255, 255, 0.2);
    --gold: #ffd21a;
    --amber: #f7a41c;
    --crowd: #000000;
  }
  html, body {
    margin: 0;
    padding: 0;
    overflow: hidden;
    background: #ffffff;
  }
  .poster {
    position: relative;
    width: 777px;
    height: 1200px;
    overflow: hidden;
    background: linear-gradient(180deg,
      var(--red-top) 0%,
      var(--red-mid) 22%,
      var(--orange-glow) 50%,
      var(--red-mid) 75%,
      var(--red-low) 90%);
    font-family: "Anton", "Impact", sans-serif;
  }
  .poster-art {
    position: absolute;
    inset: 0;
    width: 777px;
    height: 1200px;
  }
  .brand-title { fill: var(--white); font-size: 262px; }
  .slogan-ghost { fill: var(--ghost); }
  .slogan { fill: var(--white); }
  .brand-mark { fill: var(--white); font-size: 30px; }
  .brand-mark-ghost { fill: var(--ghost); font-size: 62px; }
</style>
</head>
<body>
<main class="poster">
  <svg class="poster-art" viewBox="0 0 777 1200" xmlns="http://www.w3.org/2000/svg">
    <defs>
      <linearGradient id="pour-fill" x1="0" y1="0" x2="1" y2="0">
        <stop offset="0" stop-color="#f7a41c" stop-opacity="0.85"/>
        <stop offset="0.5" stop-color="#ffe44a"/>
        <stop offset="1" stop-color="#f7a41c" stop-opacity="0.85"/>
      </linearGradient>
    </defs>

    <!-- Background slogan, large and faint -->
    <g class="slogan-ghost">
      <text transform="translate(318 245) skewX(-8)" font-size="107" textLength="432" lengthAdjust="spacingAndGlyphs">EXPERIENCE</text>
      <text transform="translate(310 362) skewX(-8)" font-size="108" textLength="128" lengthAdjust="spacingAndGlyphs">THE</text>
      <text transform="translate(300 547) skewX(-12)" font-size="204" textLength="445" lengthAdjust="spacingAndGlyphs">MAGIC</text>
    </g>

    <!-- Faint brand name, lower right -->
    <text class="brand-mark-ghost" x="598" y="985" textLength="160" lengthAdjust="spacingAndGlyphs">VANTORO</text>

    <!-- Pouring liquid illustration area -->
    <g role="img" aria-label="Golden liquid pouring from a swirling ring down into a splash above the crowd">
      <rect x="382" y="70" width="80" height="1000" rx="40" fill="url(#pour-fill)"/>
    </g>

    <!-- Vertical brand title -->
    <text class="brand-title" transform="translate(254 1040) rotate(-90)" x="0" y="0" textLength="1008" lengthAdjust="spacingAndGlyphs">VANTORO</text>

    <!-- Foreground slogan -->
    <g class="slogan">
      <text transform="translate(476 565) skewX(-8)" font-size="66" textLength="268" lengthAdjust="spacingAndGlyphs">EXPERIENCE</text>
      <text transform="translate(470 637) skewX(-8)" font-size="68" textLength="80" lengthAdjust="spacingAndGlyphs">THE</text>
      <text transform="translate(466 753) skewX(-12)" font-size="127" textLength="276" lengthAdjust="spacingAndGlyphs">MAGIC</text>
    </g>

    <!-- Brand name, lower right -->
    <text class="brand-mark" x="655" y="1058" textLength="90" lengthAdjust="spacingAndGlyphs">VANTORO</text>

    <!-- Crowd silhouette band -->
    <g role="img" aria-label="Silhouette of a cheering concert crowd with raised hands">
      <rect x="0" y="1068" width="777" height="132" fill="var(--crowd)"/>
    </g>
  </svg>
</main>
</body>
</html>
```